Natural Sunscreen Label Design for a Natural Cosmetics brand

We are looking to create a label design for a Natural Sunscreen Lotion. The labels will be a stick-on label on a white background tube. Enclosed a file with the content and some ideas/references. Please feel free to explore more.

It is important that the SPF is highlighted as large text and to use colors that give the customer an impression this being a sunscreen from far away as well.
We like white and orange/amber/yellow.
Details attached
Our Logo is attached as well as the size template of the label.

```html
<!DOCTYPE html>
<html lang="en">
<head>
<meta charset="UTF-8">
<title>Brisamar Natural Sun Lotion – Label</title>
<link href="https://fonts.googleapis.com/css2?family=Barlow+Semi+Condensed:wght@300;400;500;600;700&display=swap" rel="stylesheet">
<style>
  :root {
    --bg: #ffffff;
    --label: #efefef;
    --ink: #1f1f1f;
    --ink-soft: #3a3a3a;
    --grey: #7a7a7a;
    --orange: #e2701a;
    --orange-light: #f08a3a;
  }
  * { margin: 0; padding: 0; box-sizing: border-box; }
  html, body { width: 1200px; height: 1200px; overflow: hidden; background: var(--bg); }
  body { font-family: "Barlow Semi Condensed", sans-serif; color: var(--ink); }

  .label {
    position: absolute;
    left: 400px; top: 130px;
    width: 400px; height: 880px;
    background: var(--label);
    border-radius: 6px;
  }

  .brand {
    position: absolute;
    left: 472px; top: 272px;
    display: flex; align-items: center; gap: 10px;
    white-space: nowrap;
  }
  .brand-dot {
    width: 16px; height: 16px; border-radius: 50%;
    background: var(--orange);
    flex: none;
  }
  .brand-name {
    font-weight: 600; font-size: 26px; letter-spacing: 3px;
    color: var(--ink);
    line-height: 1;
  }

  .line-name {
    position: absolute; left: 486px; top: 406px;
    font-weight: 700; font-size: 29px; color: var(--orange);
    letter-spacing: 0.5px;
  }
  .product-en {
    position: absolute; left: 486px; top: 436px;
    font-weight: 600; font-size: 34px; color: var(--ink);
  }
  .product-pt {
    position: absolute; left: 486px; top: 472px;
    font-weight: 400; font-size: 31px; color: var(--ink-soft);
  }

  .spf-number {
    position: absolute; left: 489px; top: 521px;
    font-weight: 700; font-size: 144px; line-height: 1;
    letter-spacing: -4px;
    white-space: nowrap;
    background: linear-gradient(90deg, var(--orange) 0%, var(--orange-light) 100%);
    -webkit-background-clip: text; background-clip: text;
    color: transparent;
  }
  .spf-label {
    position: absolute; left: 638px; top: 540px;
    font-weight: 600; font-size: 34px; line-height: 1.2; color: var(--ink);
  }
  .spf-plus { position: absolute; left: 636px; top: 586px; }

  .use {
    position: absolute; left: 489px; top: 690px;
    font-weight: 400; font-size: 24px; color: var(--ink-soft);
  }
  .filters {
    position: absolute; left: 490px; top: 730px;
    font-weight: 600; font-size: 23px; color: var(--grey);
  }
  .claims {
    position: absolute; left: 491px; top: 776px;
    list-style: none;
    font-weight: 400; font-size: 21px; line-height: 18px; color: var(--ink-soft);
  }
  .meta {
    position: absolute; left: 495px; top: 879px;
    display: flex; align-items: center;
  }
  .vegan {
    font-weight: 700; font-size: 20px; letter-spacing: 4px; color: var(--ink-soft);
  }
  .meta-square {
    width: 13px; height: 13px; background: var(--orange);
    margin: 0 16px 0 14px;
  }
  .volume { font-weight: 400; font-size: 21px; color: var(--ink); }
</style>
</head>
<body>
  <div class="label"></div>

  <div class="brand">
    <span class="brand-dot"></span>
    <span class="brand-name">MARÉSOL LISBOA</span>
  </div>

  <div class="line-name">BRISAMAR</div>
  <div class="product-en">NATURAL SUN LOTION</div>
  <div class="product-pt">LOÇÃO SOLAR NATURAL</div>

  <div class="spf-number">30</div>
  <div class="spf-label">SPF</div>
  <svg class="spf-plus" width="58" height="60" viewBox="0 0 58 60" aria-hidden="true">
    <rect x="20" y="0" width="17" height="60" rx="2" fill="#e8792a"/>
    <rect x="0" y="21" width="58" height="17" rx="2" fill="#e8792a"/>
  </svg>

  <div class="use">For Body and Face</div>
  <div class="filters">UVA | UVB</div>
  <ul class="claims">
    <li>With BIO Aloe Vera</li>
    <li>Non-greasy</li>
    <li>Water Resistant</li>
    <li>Safe for kids and adults</li>
  </ul>

  <div class="meta">
    <span class="vegan">VEGAN</span>
    <span class="meta-square"></span>
    <span class="volume">100 ml</span>
  </div>
</body>
</html>
```